Steadfast Claimworks Website - a medical billing website - one page

I need a one-page website to attract potential clients to my medical billing services - I am in the process of creating a logo, the contest ends Friday. I also have some ideas and am writing some of the copy that I can send you.

SLOGAN: We Turn Codes Into Money

MISSION STATEMENT: Give compassionate quality service and precision medical billing with urgency

Target Market(s)

MD's, physical therapists, occupational therapists, speech therapists, chiropractors, psychologists, psychiatrists, dentists and new grads of the above

Coding

Coded - Design and coding required

Number of Pages Required

1 page

Font styles to use
Sans Serif
Decorative
Script

Colors
33a6d7
add136
87cfc6
cadf82
9bcb3c
85cae6

Requirements
Must have
• I am working on the major points of copy that I need, plus
• ranking search terms keywords and phrases
Nice to have
• creativity to draw clients in
• my color choices below are similar to the logo coloring - but if you like something different feel free to use your own creative colors.

```html
<!DOCTYPE html>
<html lang="en">
<head>
<meta charset="utf-8">
<title>Steadfast Claimworks — Medical Billing</title>
<link href="https://fonts.googleapis.com/css2?family=Lato:wght@400;700;900&display=swap" rel="stylesheet">
<style>
:root{
  --blue:#2e8fd2;
  --green:#8dc63f;
  --sky:#74bfe4;
  --orange:#f26a21;
  --ink:#222;
  --text:#3a3a3a;
  --muted:#666;
  --card:#f4f4f4;
  --footer:#232323;
  --band:linear-gradient(100deg,#2b8fd3 0%,#3f9fae 35%,#6cb65a 70%,#8dc63f 100%);
  --btn:linear-gradient(180deg,#8dc63f 0%,#4fb07a 55%,#2e9bd0 100%);
}
*{box-sizing:border-box;margin:0;padding:0}
html,body{width:738px;height:1200px;overflow:hidden;background:#000;font-family:'Lato',sans-serif}
.canvas{position:relative;width:738px;height:1200px;background:#000}
.frame{position:absolute;top:17px;width:300px;height:1166px;overflow:hidden}
.frame--main{left:48px}
.frame--popup{left:389px}
.page{position:absolute;left:0;top:0;width:614px;height:2387px;background:#fff;transform:scale(0.4886);transform-origin:0 0;overflow:hidden;color:var(--text)}
.abs{position:absolute}
.bands{position:absolute;left:0;top:0;width:614px;height:2387px}
/* header */
.header{position:absolute;left:0;top:0;width:614px;height:42px;background:#fff;z-index:3}
.brand{position:absolute;left:38px;top:12px;font-size:17px;font-weight:900;color:var(--blue)}
.nav{position:absolute;top:15px;font-size:9px;font-weight:700;color:#333}
.nav--active{top:12px;left:233px;width:44px;height:18px;line-height:18px;text-align:center;border-radius:9px;background:var(--btn);color:#fff}
/* hero */
.hero-title{left:38px;top:218px;font-size:36px;font-weight:900;color:#fff;z-index:2;white-space:nowrap}
.hero-sub{left:38px;top:257px;width:270px;font-size:13.5px;font-weight:700;line-height:16px;color:#fff;z-index:2}
.btn{display:block;border-radius:12px;background:var(--btn);color:#fff;font-weight:700;text-align:center;box-shadow:0 2px 3px rgba(0,0,0,.25)}
.hero-btn{left:38px;top:300px;width:85px;height:23px;line-height:23px;font-size:9.5px;z-index:2}
.photo{position:absolute}
/* about */
.about-card{left:220px;top:483px;width:357px;height:223px;background:var(--card);box-shadow:0 2px 8px rgba(0,0,0,.18)}
.about-title{left:101px;top:20px;font-size:14.5px;font-weight:700;color:var(--ink)}
.about-copy{left:101px;top:48px;width:240px;font-size:6.8px;line-height:14.3px;color:#444}
.about-copy p+p{margin-top:6px}
.about-btn{left:101px;top:176px;width:85px;height:23px;line-height:23px;font-size:9.5px}
/* services */
.section-title{width:614px;text-align:center;font-size:14px;font-weight:700;color:#fff}
.section-sub{width:614px;text-align:center;font-size:7.6px;color:#eaf6ea}
.svc{top:886px;width:124px;height:126px;background:#fff;border-radius:3px;box-shadow:0 2px 5px rgba(0,0,0,.2);overflow:hidden}
.svc-photo{height:96px}
.svc-label{height:30px;line-height:30px;text-align:center;font-size:9.6px;font-weight:700;color:#333}
.chev{font-size:17px;color:#fff;font-weight:400}
/* lists */
.list-title{font-size:14px;font-weight:700;line-height:17px;color:var(--ink)}
.item{height:38px;display:flex;align-items:center}
.item-icon{width:38px;height:38px;flex:none}
.item-label{margin-left:9px;font-size:8px;color:#444}
/* testimonials */
.quote{left:74px;top:1798px;width:466px;text-align:center;font-size:7.6px;line-height:15.6px;color:#eaf6ea}
.avatar{left:284px;top:1855px;width:44px;height:44px;border-radius:50%;background:linear-gradient(160deg,#c7dbe8,#ffffff 55%,#5b84a6);border:2px solid #fff}
.t-name{width:614px;top:1906px;text-align:center;font-size:9px;font-weight:700;color:#fff}
.t-loc{width:614px;top:1919px;text-align:center;font-size:7.6px;color:#eaf6ea}
/* blog */
.blog{left:38px;top:1952px;width:538px;height:206px;background:#fff;border-radius:3px;box-shadow:0 2px 8px rgba(0,0,0,.18)}
.blog-title{left:0;top:20px;width:538px;text-align:center;font-size:14px;font-weight:700;color:var(--ink)}
.post{top:51px;width:156px}
.post-photo{height:90px;border-radius:2px}
.post-title{margin-top:10px;font-size:8.6px;font-weight:700;line-height:13px;color:#333}
.post-date{margin-top:4px;font-size:7px;font-weight:700;color:var(--blue)}
/* signup */
.signup{left:0;top:2195px;width:614px;height:47px;background:var(--sky)}
.signup-title{left:116px;top:12px;font-size:17px;font-weight:700;color:#fff}
.signup-input{left:235px;top:12px;width:186px;height:22px;background:#fff;font-size:6.6px;line-height:22px;padding-left:7px;color:#444}
.signup-btn{left:428px;top:12px;width:69px;height:22px;line-height:22px;text-align:center;background:var(--orange);color:#fff;font-size:8.6px;font-weight:700}
/* footer */
.footer{left:0;top:2242px;width:614px;height:145px;background:var(--footer);color:#cfcfcf}
.f-brand{left:38px;top:24px;font-size:16px;font-weight:900;color:#9a9a9a}
.f-text{font-size:6.6px;line-height:12px;color:#cfcfcf}
.f-head{font-size:8.6px;font-weight:700;color:var(--green)}
.f-ico{display:inline-block;width:6px;height:6px;border-radius:50%;background:var(--green);margin-right:10px;vertical-align:middle}
.social{top:32px;left:452px;display:flex;gap:11px}
.social span{width:9px;height:9px;border-radius:50%;background:#9a9a9a}
/* popup */
.overlay{left:0;top:0;width:614px;height:2387px;background:rgba(60,60,60,.45);z-index:10}
.modal{left:153px;top:177px;width:308px;height:156px;background:#fff;border-radius:5px;z-index:11;box-shadow:0 4px 14px rgba(0,0,0,.35)}
.modal-title{left:0;top:18px;width:308px;text-align:center;font-size:15.5px;font-weight:700;line-height:22px;color:var(--ink)}
.modal-close{right:8px;top:4px;font-size:10px;font-weight:700;color:#333}
.modal-input{left:29px;top:75px;width:252px;height:25px;border-radius:13px;border:1px solid #ccc;box-shadow:0 1px 3px rgba(0,0,0,.15);text-align:center;line-height:23px;font-size:7.6px;color:#333}
.modal-btn{left:29px;top:110px;width:252px;height:25px;line-height:25px;font-size:10.5px}
</style>
</head>
<body>
<div class="canvas">

<!-- ===== Page: default state ===== -->
<div class="frame frame--main">
<div class="page">
  <svg class="bands" viewBox="0 0 614 2387" aria-hidden="true">
    <defs>
      <linearGradient id="bandA" x1="0" y1="0" x2="1" y2="0.2">
        <stop offset="0" stop-color="#2b8fd3"/><stop offset=".45" stop-color="#4fa99a"/><stop offset="1" stop-color="#8dc63f"/>
      </linearGradient>
      <linearGradient id="heroA" x1="0" y1="0" x2="1" y2="1">
        <stop offset="0" stop-color="#7d8a99"/><stop offset=".45" stop-color="#a7a39a"/><stop offset=".75" stop-color="#c98a55"/><stop offset="1" stop-color="#6f7f92"/>
      </linearGradient>
    </defs>
    <path d="M0,388 C60,438 140,462 220,448 C300,433 330,398 420,393 C520,388 580,368 614,338 V42 H0Z" fill="#1c1c1c"/>
    <path d="M0,380 C60,430 140,455 220,440 C300,425 330,390 420,385 C520,380 580,360 614,330 V42 H0Z" fill="url(#heroA)"/>
    <path d="M0,750 C80,790 180,810 260,805 C380,800 480,780 614,730 V1090 C540,1110 440,1110 380,1095 C300,1070 220,1040 150,1068 C100,1090 50,1115 0,1125Z" fill="url(#bandA)"/>
    <path d="M0,1730 C60,1700 120,1680 210,1690 C300,1700 380,1745 460,1745 C530,1745 580,1715 614,1690 V2195 H300 C200,2190 80,2150 0,2100Z" fill="url(#bandA)"/>
  </svg>
  <div class="abs" role="img" aria-label="Hero photo: physician and colleagues reviewing a tablet in a clinic meeting" style="left:0;top:42px;width:614px;height:340px"></div>

  <header class="header">
    <div class="brand">Steadfast Claimworks</div>
    <span class="nav nav--active abs">Home</span>
    <span class="nav" style="left:288px">About Us</span>
    <span class="nav" style="left:345px">Services</span>
    <span class="nav" style="left:399px">Benefits</span>
    <span class="nav" style="left:452px">Blog</span>
    <span class="nav" style="left:490px">Reviews</span>
    <span class="nav" style="left:544px">Contact</span>
  </header>

  <h1 class="abs hero-title">Steadfast Claimworks</h1>
  <p class="abs hero-sub">Sed rutrum odio quam, sed commodo ex sollicitudin vulputate.</p>
  <span class="abs btn hero-btn">Read More</span>

  <div class="photo" role="img" aria-label="Photo: doctors working together at a laptop" style="left:0;top:480px;width:300px;height:227px;background:linear-gradient(120deg,#b9c9d6,#e6eef3 45%,#8fa4b6);clip-path:polygon(0 0,100% 4%,100% 96%,0 100%)"></div>
  <section class="abs about-card">
    <h2 class="abs about-title">About Steadfast Claimworks</h2>
    <div class="abs about-copy">
      <p>Sed rutrum odio quam, sed commodo ex sollicitudin vulputate. Etiam id tortor non lorem volutpat ultrices. Pellentesque ac pellentesque sem, a consequat turpis. Integer leo magna, bibendum eget tristique non, egestas vitae nunc.</p>
      <p>Nunc et scelerisque nulla, a mattis libero. Suspendisse fermentum porta odio. Nam et commodo odio, ut auctor risus. Nam euismod urna risus, quis pellentesque massa dapibus et. Nam sit amet ipsum lobortis, facilisis lorem ac, consectetur ex</p>
    </div>
    <span class="abs btn about-btn">Read More</span>
  </section>

  <h2 class="abs section-title" style="top:826px">Service Area For</h2>
  <p class="abs section-sub" style="top:852px">Sed rutrum odio quam, sed commodo ex sollicitudin vulputate. Etiam id tortor non lorem volutpat ultrices</p>
  <span class="abs chev" style="left:22px;top:936px">&#8249;</span>
  <span class="abs chev" style="left:583px;top:936px">&#8250;</span>
  <div class="abs svc" style="left:38px"><div class="svc-photo" role="img" aria-label="Photo: physical therapist with clipboard" style="background:linear-gradient(160deg,#e2e6ea,#b8c6d2)"></div><div class="svc-label">Physical Therapists</div></div>
  <div class="abs svc" style="left:176px"><div class="svc-photo" role="img" aria-label="Photo: speech therapist in session" style="background:linear-gradient(160deg,#eeeae6,#9c8f86)"></div><div class="svc-label">Speech Therapists</div></div>
  <div class="abs svc" style="left:314px"><div class="svc-photo" role="img" aria-label="Photo: chiropractor in blue scrubs" style="background:linear-gradient(160deg,#d9dde2,#3f6fb0)"></div><div class="svc-label">Chiropractors</div></div>
  <div class="abs svc" style="left:452px"><div class="svc-photo" role="img" aria-label="Photo: psychologist in office" style="background:linear-gradient(160deg,#a8735a,#8b8d92)"></div><div class="svc-label">Psychologists</div></div>

  <h2 class="abs list-title" style="left:38px;top:1144px;width:260px">Medical billing companies can take care of crucial tasks like:</h2>
  <div class="abs" style="left:38px;top:1189px">
    <div class="item"><svg class="item-icon" viewBox="0 0 38 38"><circle cx="19" cy="19" r="17.5" fill="none" stroke="url(#bandA)" stroke-width="1.6"/><rect x="12" y="11" width="12" height="16" rx="1" fill="none" stroke="#333"/><path d="M14 15h8M14 18h8M14 21h5" stroke="#333"/><circle cx="25" cy="25" r="3" fill="none" stroke="#333"/></svg><span class="item-label">Patient Insurance Verification</span></div>
    <div class="item" style="margin-top:12px"><svg class="item-icon" viewBox="0 0 38 38"><circle cx="19" cy="19" r="17.5" fill="none" stroke="url(#bandA)" stroke-width="1.6"/><rect x="11" y="12" width="16" height="11" rx="1" fill="none" stroke="#333"/><path d="M17 15l-2 2.5 2 2.5M21 15l2 2.5-2 2.5M14 26h10" stroke="#333" fill="none"/></svg><span class="item-label">Medical Coding</span></div>
    <div class="item" style="margin-top:12px"><svg class="item-icon" viewBox="0 0 38 38"><circle cx="19" cy="19" r="17.5" fill="none" stroke="url(#bandA)" stroke-width="1.6"/><rect x="11" y="12" width="16" height="11" rx="1" fill="none" stroke="#333"/><path d="M14 16h5M14 19h3M21 15v5h3M15 26h8" stroke="#333" fill="none"/></svg><span class="item-label">Claim Tracking</span></div>
    <div class="item" style="margin-top:12px"><svg class="item-icon" viewBox="0 0 38 38"><circle cx="19" cy="19" r="17.5" fill="none" stroke="url(#bandA)" stroke-width="1.6"/><rect x="12" y="11" width="13" height="16" rx="1" fill="none" stroke="#333"/><path d="M15 23v-3M18 23v-6M21 23v-4" stroke="#333"/><circle cx="24" cy="24" r="3" fill="none" stroke="#333"/></svg><span class="item-label">Billing Analytics &amp; Reports</span></div>
  </div>
  <div class="photo" role="img" aria-label="Photo: two doctors reviewing patient notes on a tablet" style="left:314px;top:1145px;width:300px;height:225px;background:linear-gradient(120deg,#d6dde3,#6f86a3 50%,#2f5fb0);clip-path:polygon(0 8%,100% 0,100% 100%,0 92%)"></div>

  <div class="photo" role="img" aria-label="Photo: doctor and nurse taking a patient's blood pressure" style="left:0;top:1410px;width:300px;height:225px;background:linear-gradient(120deg,#c5ced6,#eef1f3 45%,#9fb1c4);clip-path:polygon(0 0,100% 6%,100% 94%,0 100%)"></div>
  <h2 class="abs list-title" style="left:314px;top:1410px;width:260px">Benefits of outsourcing medical billing include:</h2>
  <div class="abs" style="left:314px;top:1455px">
    <div class="item"><svg class="item-icon" viewBox="0 0 38 38"><circle cx="19" cy="19" r="17.5" fill="none" stroke="url(#bandA)" stroke-width="1.6"/><rect x="12" y="11" width="12" height="16" rx="1" fill="none" stroke="#333"/><path d="M14 15h8M14 18h5" stroke="#333"/><circle cx="23" cy="24" r="4" fill="none" stroke="#333"/></svg><span class="item-label">Simplifying financial record-keeping</span></div>
    <div class="item" style="margin-top:12px"><svg class="item-icon" viewBox="0 0 38 38"><circle cx="19" cy="19" r="17.5" fill="none" stroke="url(#bandA)" stroke-width="1.6"/><rect x="11" y="11" width="13" height="15" rx="1" fill="none" stroke="#333"/><path d="M13 15h8M13 18h8" stroke="#333"/><rect x="21" y="22" width="6" height="5" fill="none" stroke="#333"/></svg><span class="item-label">Data protection for sensitive files</span></div>
    <div class="item" style="margin-top:12px"><svg class="item-icon" viewBox="0 0 38 38"><circle cx="19" cy="19" r="17.5" fill="none" stroke="url(#bandA)" stroke-width="1.6"/><path d="M11 27h16M13 27v-4M17 27v-6M21 27v-8M25 27v-11M12 20l5-4 4 2 5-6" stroke="#333" fill="none"/></svg><span class="item-label">High accuracy</span></div>
    <div class="item" style="margin-top:12px"><svg class="item-icon" viewBox="0 0 38 38"><circle cx="19" cy="19" r="17.5" fill="none" stroke="url(#bandA)" stroke-width="1.6"/><rect x="12" y="11" width="14" height="16" rx="1" fill="none" stroke="#333"/><circle cx="19" cy="19" r="4.5" fill="none" stroke="#333"/><path d="M19 16.5v2.5h2" stroke="#333" fill="none"/></svg><span class="item-label">Quick turnaround time for insurance claims</span></div>
  </div>

  <h2 class="abs section-title" style="top:1772px">Testimonials</h2>
  <p class="abs quote">" Sed rutrum odio quam, sed commodo ex sollicitudin vulputate. Etiam id tortor non lorem volutpat ultrices rutrum odio quam, sed commodo ex sollicitudin vulputate. Etiam id tortor non lorem volutpat ultrices. Pellentesque ac pellentesque sem, a consequat turpis. Integer leo magna, bibendum eget tristique non..."</p>
  <span class="abs chev" style="left:247px;top:1864px">&#8249;</span>
  <span class="abs chev" style="left:359px;top:1864px">&#8250;</span>
  <div class="abs avatar" role="img" aria-label="Portrait of the reviewer"></div>
  <p class="abs t-name">Name Heading</p>
  <p class="abs t-loc">Location</p>

  <section class="abs blog">
    <h2 class="abs blog-title">Blog Posts</h2>
    <article class="abs post" style="left:13px"><div class="post-photo" role="img" aria-label="Photo: medical staff reviewing a tablet" style="background:linear-gradient(120deg,#dfe6ec,#7d98c4)"></div><h3 class="post-title">Etiam id tortor non lorem volutpat ultrices pellentesque.</h3><p class="post-date">January 25, 2020</p></article>
    <article class="abs post" style="left:191px"><div class="post-photo" role="img" aria-label="Photo: patient at a clinic reception desk" style="background:linear-gradient(120deg,#efe9e6,#c7b8b3)"></div><h3 class="post-title">Etiam id tortor non lorem volutpat ultrices pellentesque.</h3><p class="post-date">January 25, 2020</p></article>
    <article class="abs post" style="left:368px"><div class="post-photo" role="img" aria-label="Photo: doctor working at a laptop" style="background:linear-gradient(120deg,#e7ecef,#b6c3cc)"></div><h3 class="post-title">Etiam id tortor non lorem volutpat ultrices pellentesque.</h3><p class="post-date">January 25, 2020</p></article>
  </section>

  <section class="abs signup">
    <h2 class="abs signup-title">Email Sign Up</h2>
    <div class="abs signup-input">Enter Email Address</div>
    <div class="abs signup-btn">Sign Up</div>
  </section>

  <footer class="abs footer">
    <div class="abs f-brand">Steadfast Claimworks</div>
    <p class="abs f-text" style="left:38px;top:54px">Suite 4, Harbor Row, 18 Lindell Ave<br>(corner of Merrow St)<br>Calder Point, NSW 2190</p>
    <p class="abs f-text" style="left:38px;top:92px"><span class="f-ico"></span>1-800-555-0142</p>
    <p class="abs f-text" style="left:38px;top:106px"><span class="f-ico"></span>hello@steadfastclaimworks.test</p>
    <h3 class="abs f-head" style="left:198px;top:24px">Site Map</h3>
    <p class="abs f-text" style="left:198px;top:42px;line-height:16px">Home<br>About Us<br>Services<br>Benefits</p>
    <p class="abs f-text" style="left:264px;top:42px;line-height:16px">Blog<br>Reviews<br>Contact</p>
    <h3 class="abs f-head" style="left:335px;top:24px">Resources</h3>
    <p class="abs f-text" style="left:335px;top:42px;line-height:16px">Sed rutrum odio<br>Quam sed commodo<br>Sollicitudin<br>Vulputate sodales</p>
    <div class="abs social" aria-label="Social links"><span></span><span></span><span></span><span></span><span></span></div>
    <p class="abs f-text" style="left:452px;top:52px">Copyright © 2020 Company Name.<br>All Right Reserved</p>
  </footer>
</div>
</div>

<!-- ===== Page: sign-up popup state ===== -->
<div class="frame frame--popup">
<div class="page">
  <svg class="bands" viewBox="0 0 614 2387" aria-hidden="true">
    <defs>
      <linearGradient id="bandB" x1="0" y1="0" x2="1" y2="0.2">
        <stop offset="0" stop-color="#2b8fd3"/><stop offset=".45" stop-color="#4fa99a"/><stop offset="1" stop-color="#8dc63f"/>
      </linearGradient>
      <linearGradient id="heroB" x1="0" y1="0" x2="1" y2="1">
        <stop offset="0" stop-color="#7d8a99"/><stop offset=".45" stop-color="#a7a39a"/><stop offset=".75" stop-color="#c98a55"/><stop offset="1" stop-color="#6f7f92"/>
      </linearGradient>
    </defs>
    <path d="M0,388 C60,438 140,462 220,448 C300,433 330,398 420,393 C520,388 580,368 614,338 V42 H0Z" fill="#1c1c1c"/>
    <path d="M0,380 C60,430 140,455 220,440 C300,425 330,390 420,385 C520,380 580,360 614,330 V42 H0Z" fill="url(#heroB)"/>
    <path d="M0,750 C80,790 180,810 260,805 C380,800 480,780 614,730 V1090 C540,1110 440,1110 380,1095 C300,1070 220,1040 150,1068 C100,1090 50,1115 0,1125Z" fill="url(#bandB)"/>
    <path d="M0,1730 C60,1700 120,1680 210,1690 C300,1700 380,1745 460,1745 C530,1745 580,1715 614,1690 V2195 H300 C200,2190 80,2150 0,2100Z" fill="url(#bandB)"/>
  </svg>
  <div class="abs" role="img" aria-label="Hero photo: physician and colleagues reviewing a tablet in a clinic meeting" style="left:0;top:42px;width:614px;height:340px"></div>

  <header class="header">
    <div class="brand">Steadfast Claimworks</div>
    <span class="nav nav--active abs">Home</span>
    <span class="nav" style="left:288px">About Us</span>
    <span class="nav" style="left:345px">Services</span>
    <span class="nav" style="left:399px">Benefits</span>
    <span class="nav" style="left:452px">Blog</span>
    <span class="nav" style="left:490px">Reviews</span>
    <span class="nav" style="left:544px">Contact</span>
  </header>

  <h1 class="abs hero-title">Steadfast Claimworks</h1>
  <p class="abs hero-sub">Sed rutrum odio quam, sed commodo ex sollicitudin vulputate.</p>
  <span class="abs btn hero-btn">Read More</span>

  <div class="photo" role="img" aria-label="Photo: doctors working together at a laptop" style="left:0;top:480px;width:300px;height:227px;background:linear-gradient(120deg,#b9c9d6,#e6eef3 45%,#8fa4b6);clip-path:polygon(0 0,100% 4%,100% 96%,0 100%)"></div>
  <section class="abs about-card">
    <h2 class="abs about-title">About Steadfast Claimworks</h2>
    <div class="abs about-copy">
      <p>Sed rutrum odio quam, sed commodo ex sollicitudin vulputate. Etiam id tortor non lorem volutpat ultrices. Pellentesque ac pellentesque sem, a consequat turpis. Integer leo magna, bibendum eget tristique non, egestas vitae nunc.</p>
      <p>Nunc et scelerisque nulla, a mattis libero. Suspendisse fermentum porta odio. Nam et commodo odio, ut auctor risus. Nam euismod urna risus, quis pellentesque massa dapibus et. Nam sit amet ipsum lobortis, facilisis lorem ac, consectetur ex</p>
    </div>
    <span class="abs btn about-btn">Read More</span>
  </section>

  <h2 class="abs section-title" style="top:826px">Service Area For</h2>
  <p class="abs section-sub" style="top:852px">Sed rutrum odio quam, sed commodo ex sollicitudin vulputate. Etiam id tortor non lorem volutpat ultrices</p>
  <span class="abs chev" style="left:22px;top:936px">&#8249;</span>
  <span class="abs chev" style="left:583px;top:936px">&#8250;</span>
  <div class="abs svc" style="left:38px"><div class="svc-photo" role="img" aria-label="Photo: physical therapist with clipboard" style="background:linear-gradient(160deg,#e2e6ea,#b8c6d2)"></div><div class="svc-label">Physical Therapists</div></div>
  <div class="abs svc" style="left:176px"><div class="svc-photo" role="img" aria-label="Photo: speech therapist in session" style="background:linear-gradient(160deg,#eeeae6,#9c8f86)"></div><div class="svc-label">Speech Therapists</div></div>
  <div class="abs svc" style="left:314px"><div class="svc-photo" role="img" aria-label="Photo: chiropractor in blue scrubs" style="background:linear-gradient(160deg,#d9dde2,#3f6fb0)"></div><div class="svc-label">Chiropractors</div></div>
  <div class="abs svc" style="left:452px"><div class="svc-photo" role="img" aria-label="Photo: psychologist in office" style="background:linear-gradient(160deg,#a8735a,#8b8d92)"></div><div class="svc-label">Psychologists</div></div>

  <h2 class="abs list-title" style="left:38px;top:1144px;width:260px">Medical billing companies can take care of crucial tasks like:</h2>
  <div class="abs" style="left:38px;top:1189px">
    <div class="item"><svg class="item-icon" viewBox="0 0 38 38"><circle cx="19" cy="19" r="17.5" fill="none" stroke="url(#bandB)" stroke-width="1.6"/><rect x="12" y="11" width="12" height="16" rx="1" fill="none" stroke="#333"/><path d="M14 15h8M14 18h8M14 21h5" stroke="#333"/><circle cx="25" cy="25" r="3" fill="none" stroke="#333"/></svg><span class="item-label">Patient Insurance Verification</span></div>
    <div class="item" style="margin-top:12px"><svg class="item-icon" viewBox="0 0 38 38"><circle cx="19" cy="19" r="17.5" fill="none" stroke="url(#bandB)" stroke-width="1.6"/><rect x="11" y="12" width="16" height="11" rx="1" fill="none" stroke="#333"/><path d="M17 15l-2 2.5 2 2.5M21 15l2 2.5-2 2.5M14 26h10" stroke="#333" fill="none"/></svg><span class="item-label">Medical Coding</span></div>
    <div class="item" style="margin-top:12px"><svg class="item-icon" viewBox="0 0 38 38"><circle cx="19" cy="19" r="17.5" fill="none" stroke="url(#bandB)" stroke-width="1.6"/><rect x="11" y="12" width="16" height="11" rx="1" fill="none" stroke="#333"/><path d="M14 16h5M14 19h3M21 15v5h3M15 26h8" stroke="#333" fill="none"/></svg><span class="item-label">Claim Tracking</span></div>
    <div class="item" style="margin-top:12px"><svg class="item-icon" viewBox="0 0 38 38"><circle cx="19" cy="19" r="17.5" fill="none" stroke="url(#bandB)" stroke-width="1.6"/><rect x="12" y="11" width="13" height="16" rx="1" fill="none" stroke="#333"/><path d="M15 23v-3M18 23v-6M21 23v-4" stroke="#333"/><circle cx="24" cy="24" r="3" fill="none" stroke="#333"/></svg><span class="item-label">Billing Analytics &amp; Reports</span></div>
  </div>
  <div class="photo" role="img" aria-label="Photo: two doctors reviewing patient notes on a tablet" style="left:314px;top:1145px;width:300px;height:225px;background:linear-gradient(120deg,#d6dde3,#6f86a3 50%,#2f5fb0);clip-path:polygon(0 8%,100% 0,100% 100%,0 92%)"></div>

  <div class="photo" role="img" aria-label="Photo: doctor and nurse taking a patient's blood pressure" style="left:0;top:1410px;width:300px;height:225px;background:linear-gradient(120deg,#c5ced6,#eef1f3 45%,#9fb1c4);clip-path:polygon(0 0,100% 6%,100% 94%,0 100%)"></div>
  <h2 class="abs list-title" style="left:314px;top:1410px;width:260px">Benefits of outsourcing medical billing include:</h2>
  <div class="abs" style="left:314px;top:1455px">
    <div class="item"><svg class="item-icon" viewBox="0 0 38 38"><circle cx="19" cy="19" r="17.5" fill="none" stroke="url(#bandB)" stroke-width="1.6"/><rect x="12" y="11" width="12" height="16" rx="1" fill="none" stroke="#333"/><path d="M14 15h8M14 18h5" stroke="#333"/><circle cx="23" cy="24" r="4" fill="none" stroke="#333"/></svg><span class="item-label">Simplifying financial record-keeping</span></div>
    <div class="item" style="margin-top:12px"><svg class="item-icon" viewBox="0 0 38 38"><circle cx="19" cy="19" r="17.5" fill="none" stroke="url(#bandB)" stroke-width="1.6"/><rect x="11" y="11" width="13" height="15" rx="1" fill="none" stroke="#333"/><path d="M13 15h8M13 18h8" stroke="#333"/><rect x="21" y="22" width="6" height="5" fill="none" stroke="#333"/></svg><span class="item-label">Data protection for sensitive files</span></div>
    <div class="item" style="margin-top:12px"><svg class="item-icon" viewBox="0 0 38 38"><circle cx="19" cy="19" r="17.5" fill="none" stroke="url(#bandB)" stroke-width="1.6"/><path d="M11 27h16M13 27v-4M17 27v-6M21 27v-8M25 27v-11M12 20l5-4 4 2 5-6" stroke="#333" fill="none"/></svg><span class="item-label">High accuracy</span></div>
    <div class="item" style="margin-top:12px"><svg class="item-icon" viewBox="0 0 38 38"><circle cx="19" cy="19" r="17.5" fill="none" stroke="url(#bandB)" stroke-width="1.6"/><rect x="12" y="11" width="14" height="16" rx="1" fill="none" stroke="#333"/><circle cx="19" cy="19" r="4.5" fill="none" stroke="#333"/><path d="M19 16.5v2.5h2" stroke="#333" fill="none"/></svg><span class="item-label">Quick turnaround time for insurance claims</span></div>
  </div>

  <h2 class="abs section-title" style="top:1772px">Testimonials</h2>
  <p class="abs quote">" Sed rutrum odio quam, sed commodo ex sollicitudin vulputate. Etiam id tortor non lorem volutpat ultrices rutrum odio quam, sed commodo ex sollicitudin vulputate. Etiam id tortor non lorem volutpat ultrices. Pellentesque ac pellentesque sem, a consequat turpis. Integer leo magna, bibendum eget tristique non..."</p>
  <span class="abs chev" style="left:247px;top:1864px">&#8249;</span>
  <span class="abs chev" style="left:359px;top:1864px">&#8250;</span>
  <div class="abs avatar" role="img" aria-label="Portrait of the reviewer"></div>
  <p class="abs t-name">Name Heading</p>
  <p class="abs t-loc">Location</p>

  <section class="abs blog">
    <h2 class="abs blog-title">Blog Posts</h2>
    <article class="abs post" style="left:13px"><div class="post-photo" role="img" aria-label="Photo: medical staff reviewing a tablet" style="background:linear-gradient(120deg,#dfe6ec,#7d98c4)"></div><h3 class="post-title">Etiam id tortor non lorem volutpat ultrices pellentesque.</h3><p class="post-date">January 25, 2020</p></article>
    <article class="abs post" style="left:191px"><div class="post-photo" role="img" aria-label="Photo: patient at a clinic reception desk" style="background:linear-gradient(120deg,#efe9e6,#c7b8b3)"></div><h3 class="post-title">Etiam id tortor non lorem volutpat ultrices pellentesque.</h3><p class="post-date">January 25, 2020</p></article>
    <article class="abs post" style="left:368px"><div class="post-photo" role="img" aria-label="Photo: doctor working at a laptop" style="background:linear-gradient(120deg,#e7ecef,#b6c3cc)"></div><h3 class="post-title">Etiam id tortor non lorem volutpat ultrices pellentesque.</h3><p class="post-date">January 25, 2020</p></article>
  </section>

  <section class="abs signup">
    <h2 class="abs signup-title">Email Sign Up</h2>
    <div class="abs signup-input">Enter Email Address</div>
    <div class="abs signup-btn">Sign Up</div>
  </section>

  <footer class="abs footer">
    <div class="abs f-brand">Steadfast Claimworks</div>
    <p class="abs f-text" style="left:38px;top:54px">Suite 4, Harbor Row, 18 Lindell Ave<br>(corner of Merrow St)<br>Calder Point, NSW 2190</p>
    <p class="abs f-text" style="left:38px;top:92px"><span class="f-ico"></span>1-800-555-0142</p>
    <p class="abs f-text" style="left:38px;top:106px"><span class="f-ico"></span>hello@steadfastclaimworks.test</p>
    <h3 class="abs f-head" style="left:198px;top:24px">Site Map</h3>
    <p class="abs f-text" style="left:198px;top:42px;line-height:16px">Home<br>About Us<br>Services<br>Benefits</p>
    <p class="abs f-text" style="left:264px;top:42px;line-height:16px">Blog<br>Reviews<br>Contact</p>
    <h3 class="abs f-head" style="left:335px;top:24px">Resources</h3>
    <p class="abs f-text" style="left:335px;top:42px;line-height:16px">Sed rutrum odio<br>Quam sed commodo<br>Sollicitudin<br>Vulputate sodales</p>
    <div class="abs social" aria-label="Social links"><span></span><span></span><span></span><span></span><span></span></div>
    <p class="abs f-text" style="left:452px;top:52px">Copyright © 2020 Company Name.<br>All Right Reserved</p>
  </footer>

  <div class="abs overlay"></div>
  <div class="abs modal" role="dialog" aria-label="Free trial offer">
    <span class="abs modal-close">×</span>
    <h2 class="abs modal-title">Get your 1 st 30 days of billing for<br>FREE – no obligations</h2>
    <div class="abs modal-input">Enter Email Address</div>
    <span class="abs btn modal-btn">Sign Up Now</span>
  </div>
</div>
</div>

</div>
</body>
</html>
```